Business Card Needed for Tend A Patron card should be modern looking with black backgroun

We need a business card designed for a company called Tend A Patron. The business card should have a black background and use our exact logo which is attached. The contact information should be green font. We have additional logo files if needed. The business card should include our logo, our slogan and our contact information.

Target Market(s)

Sales Professionals

Industry/Entity Type

Business

Contact Information for Business Card

Use the information on our website www.tendapatron-example.com for contact information. The card should also have our slogan "Let us help you plant your referral seed.."

Requirements
Must have
• Black Background with Green Logo and Font

```html
<!DOCTYPE html>
<html lang="en">
<head>
<meta charset="utf-8">
<title>Tend A Patron – Business Card</title>
<link href="https://fonts.googleapis.com/css2?family=Cinzel:wght@500&family=Questrial&family=Didact+Gothic&display=swap" rel="stylesheet">
<style>
  :root {
    --backdrop: #e9e6e2;
    --card-black: #050505;
    --card-wave: #1b1b1b;
    --brand-green: #1e9c4d;
    --name-grey: #5a5a5a;
    --text-grey: #9a9a9a;
  }
  * { margin: 0; padding: 0; box-sizing: border-box; }
  html, body { width: 1200px; height: 1000px; overflow: hidden; }
  body { background: var(--backdrop); position: relative; font-family: "Questrial", "Century Gothic", sans-serif; }

  .card {
    position: absolute; left: 265px; width: 665px; height: 398px;
    background: var(--card-black); overflow: hidden;
    box-shadow: 0 6px 18px rgba(0,0,0,.25);
  }
  .card--front { top: 72px; }
  .card--back { top: 532px; }

  .edge-rule { position: absolute; top: 0; bottom: 0; width: 3px; background: var(--brand-green); }
  .edge-rule--left { left: 19px; }
  .edge-rule--right { right: 19px; }

  .brand-mark {
    position: absolute; border-radius: 50%;
    background: radial-gradient(circle at 45% 40%, #22a556, #126b34);
  }
  .card--front .brand-mark { left: 252px; top: 33px; width: 160px; height: 160px; }
  .card--back .brand-mark { left: 380px; top: 46px; width: 144px; height: 144px; }

  .brand-name {
    position: absolute; font-family: "Cinzel", serif; font-weight: 500;
    color: var(--name-grey); white-space: nowrap; text-align: center;
    letter-spacing: 1px;
  }
  .card--front .brand-name { left: 0; right: 0; top: 208px; font-size: 46px; }
  .card--back .brand-name { left: 287px; width: 346px; top: 174px; font-size: 40px; }

  .slogan {
    position: absolute; left: 0; right: 0; top: 306px; text-align: center;
    color: var(--brand-green); font-size: 17.5px; letter-spacing: .3px;
  }

  .back-waves { position: absolute; inset: 0; }

  .contact { position: absolute; left: 33px; top: 250px; font-family: "Didact Gothic", "Century Gothic", sans-serif; }
  .contact__company { color: var(--brand-green); font-weight: bold; font-size: 17px; font-family: "Questrial", sans-serif; -webkit-text-stroke: .4px var(--brand-green); }
  .contact__line { color: var(--text-grey); font-size: 17px; line-height: 22px; }
  .contact__emails { margin-top: 22px; }
  .email-row { display: flex; align-items: center; color: var(--brand-green); font-size: 17px; line-height: 21px; }
  .email-row__label { font-weight: bold; -webkit-text-stroke: .4px var(--brand-green); margin-right: 7px; }
  .email-row svg { margin-right: 6px; }
</style>
</head>
<body>

<section class="card card--front">
  <div class="edge-rule edge-rule--left"></div>
  <div class="edge-rule edge-rule--right"></div>
  <div class="brand-mark" role="img" aria-label="Brand mark area"></div>
  <div class="brand-name">TEND A PATRON</div>
  <p class="slogan">Let us help you plant your referral seed</p>
</section>

<section class="card card--back">
  <svg class="back-waves" width="665" height="398" viewBox="0 0 665 398" aria-hidden="true">
    <defs>
      <linearGradient id="waveFill" x1="0" y1="0" x2="1" y2="0">
        <stop offset="0" stop-color="#0a0a0a"/>
        <stop offset="0.6" stop-color="#1c1c1c"/>
        <stop offset="1" stop-color="#262626"/>
      </linearGradient>
    </defs>
    <path d="M0 215 C180 150 300 90 470 105 C560 112 620 100 665 92 L665 398 L0 398 Z" fill="url(#waveFill)"/>
    <path d="M0 398 L0 360 C200 330 420 270 665 290 L665 398 Z" fill="#0b0b0b"/>
  </svg>
  <div class="brand-mark" role="img" aria-label="Brand mark area"></div>
  <div class="brand-name">TEND A PATRON</div>
  <div class="contact">
    <div class="contact__company">Tend A Patron , LLC</div>
    <div class="contact__line">P.O. Box 218</div>
    <div class="contact__line">Harbor Creek, MD</div>
    <div class="contact__emails">
      <div class="email-row"><span class="email-row__label">E-mail</span>
        <svg width="14" height="10" viewBox="0 0 14 10"><rect width="14" height="10" fill="#1e9c4d"/><path d="M0 0 L7 6 L14 0" fill="none" stroke="#050505" stroke-width="1.3"/></svg>
        marla@tendapatron-example.com</div>
      <div class="email-row"><span class="email-row__label">E-Mail</span>
        <svg width="14" height="10" viewBox="0 0 14 10"><rect width="14" height="10" fill="#1e9c4d"/><path d="M0 0 L7 6 L14 0" fill="none" stroke="#050505" stroke-width="1.3"/></svg>
        jodie@tendapatron-example.com</div>
    </div>
  </div>
</section>

</body>
</html>
```